TERV Business Card Neil

Field Capital Advisory (TERV) is a consulting company that advises stakeholders in the Agricultural Industry. Based in rural NSW Australia, we need a good business card. TERV has a lifetime of agricultural experience and knowledge, particularly in the beef, wool and lamb markets. Though it is expanding into other rural ventures. Our clients are primarily off-farm investors who trust our business to advise on the best path forward for their agricultural investment. We also work with large players in the retail sector. Our image is trustworthy, reliable, smart and professional.
Updates

I think the black is too urban, perhaps a dark blue on one side and white on the other, or the yellow/orange on one side and white on the other??

we need to have the tag line "Customised Agribusiness Strategy" and our list of services:

"Due Diligence, Acquisition, Planning, Management, Strategy, Supply Chain" included in the design

we actually have 6 services - the should read in order:

Due diligence
Acquisition
Strategy
Planning 
Management
Supply chain

Target Market(s)

large rural land holders
senior players in agribusiness
senior management of retail food outlets
middle-senior aged men

Industry/Entity Type

Retail

Requirements
Must have
• high quality, 2 sides

logo

"Neil Hartwick
Director
0491357208
neil@terv.com.au
PO Box 4621, Kellmore NSW 2371"

tag line "Customised Agribusiness Strategy"

services provided

"Due diligence
Acquisition
Strategy
Planning
Management
Supply chain"
Should not have
• no images of animals or leaves

```html
<!DOCTYPE html>
<html lang="en">
<head>
<meta charset="utf-8">
<title>TERV Business Card – Neil Hartwick</title>
<link rel="stylesheet" href="https://fonts.googleapis.com/css2?family=EB+Garamond:ital,wght@0,400;0,500;0,600;1,400&display=swap">
<style>
  :root {
    --backdrop: #d9d9d7;
    --card-white: #f7f7f5;
    --brand-blue: #1a4284;
    --accent-gold: #e9a21b;
    --text-grey: #555759;
    --rule-grey: #b9bcc2;
    --rule-light: rgba(255,255,255,0.45);
  }
  * { box-sizing: border-box; margin: 0; padding: 0; }
  html, body {
    width: 1200px; height: 800px; overflow: hidden;
    background: var(--backdrop);
    font-family: "EB Garamond", Georgia, serif;
  }
  .stage {
    width: 1200px; height: 800px;
    display: flex; align-items: center; justify-content: center; gap: 40px;
  }
  .card {
    width: 540px; height: 309px; position: relative;
    box-shadow: 0 6px 18px rgba(0,0,0,0.18);
  }

  /* Front: contact side */
  .card-front { background: var(--card-white); }
  .front-brand {
    position: absolute; left: 0; top: 0; width: 280px; height: 100%;
    display: flex; flex-direction: column; align-items: center; justify-content: center;
  }
  .brand-name {
    font-size: 76px; font-weight: 500; line-height: 1; letter-spacing: 2px;
    color: var(--brand-blue);
  }
  .brand-descriptor {
    margin-top: 6px; font-size: 15px; font-variant: small-caps; letter-spacing: 1px;
    color: var(--brand-blue);
  }
  .front-divider {
    position: absolute; left: 290px; top: 24px; bottom: 24px;
    width: 1px; background: var(--rule-grey);
  }
  .contact-person { position: absolute; left: 310px; top: 34px; }
  .person-name { font-size: 22px; color: var(--brand-blue); line-height: 1.1; }
  .person-role { font-size: 15px; font-style: italic; color: var(--brand-blue); }
  .contact-details {
    position: absolute; left: 310px; bottom: 26px;
    font-size: 18px; line-height: 1.25; color: var(--text-grey);
    list-style: none;
  }
  .contact-details li { display: flex; align-items: center; gap: 6px; }
  .contact-details svg { width: 16px; height: 16px; flex: none; }

  /* Back: services side */
  .card-back { background: var(--brand-blue); color: #fff; }
  .back-brand { position: absolute; top: 26px; left: 0; right: 0; text-align: center; }
  .back-brand .brand-name { color: #fff; font-size: 60px; }
  .back-brand .brand-descriptor { color: #fff; margin-top: 2px; font-size: 13px; }
  .back-rule { position: absolute; left: 60px; right: 60px; height: 1px; background: var(--rule-light); }
  .back-rule.upper { top: 112px; }
  .back-rule.lower { top: 164px; }
  .tagline {
    position: absolute; top: 138px; left: 0; right: 0; text-align: center;
    font-size: 13px; font-style: italic; color: #fff;
  }
  .service-list {
    position: absolute; top: 180px; left: 70px; right: 60px;
    display: grid; grid-template-columns: 1fr 1fr; column-gap: 40px;
    color: var(--accent-gold);
    font-size: 17px; letter-spacing: 1.5px; text-transform: uppercase; line-height: 1.2;
  }
  .service-column { list-style: none; }
  .service-column.offset { padding-top: 34px; }
</style>
</head>
<body>
<main class="stage">

  <section class="card card-front" aria-label="Business card front">
    <div class="front-brand">
      <span class="brand-name">TERV</span>
      <span class="brand-descriptor">Field Capital Advisory</span>
    </div>
    <div class="front-divider"></div>
    <div class="contact-person">
      <p class="person-name">Neil Hartwick</p>
      <p class="person-role">Director</p>
    </div>
    <ul class="contact-details">
      <li>PO Box 4621,</li>
      <li>Kellmore NSW 2371</li>
      <li>
        <svg viewBox="0 0 16 16" aria-hidden="true"><path d="M4 1.5 6 4.5 4.8 6c.8 1.8 2.3 3.4 4.2 4.2L10.5 9l3 2-1.2 2.6C7.5 13.3 2.7 8.5 2.4 3.7Z" fill="none" stroke="#555759" stroke-width="1.2"/></svg>
        (04) 9135-7208
      </li>
      <li>
        <svg viewBox="0 0 16 16" aria-hidden="true"><rect x="1.5" y="3.5" width="13" height="9" fill="none" stroke="#555759" stroke-width="1.1"/><path d="M1.5 3.5 8 9l6.5-5.5" fill="none" stroke="#555759" stroke-width="1.1"/></svg>
        neil@terv.com.au
      </li>
    </ul>
  </section>

  <section class="card card-back" aria-label="Business card back">
    <div class="back-brand">
      <span class="brand-name">TERV</span><br>
      <span class="brand-descriptor">Field Capital Advisory</span>
    </div>
    <div class="back-rule upper"></div>
    <p class="tagline">Customised Agribusiness Strategy</p>
    <div class="back-rule lower"></div>
    <div class="service-list">
      <ul class="service-column">
        <li>Due Diligence</li>
        <li>Supply Chain</li>
        <li>Management</li>
      </ul>
      <ul class="service-column offset">
        <li>Acquisition</li>
        <li>Planning</li>
        <li>Strategy</li>
      </ul>
    </div>
  </section>

</main>
</body>
</html>
```